Mouthguards and Sports Safety

I am trying to make a powerpoint presentation that will be looped as a video in my dental office's waiting room. The point of this is to raise awareness for mouthguards and to inform the viewer that we are making them. The basic text is in the attached presentation, but I need photos and interesting animations to make it appealing

```html
<!DOCTYPE html>
<html lang="en">
<head>
<meta charset="utf-8">
<title>Mouthguards and Sports Safety – Slide Overview</title>
<link href="https://fonts.googleapis.com/css2?family=Lato:wght@400&family=Hind:wght@300;400&display=swap" rel="stylesheet">
<style>
  :root {
    --bg-top: #6fb1bd;
    --bg-bottom: #4f86ad;
    --slide-deep: #4a78a8;
    --slide-teal: #7cc6c6;
    --slide-mid: #62a7bb;
    --ring: rgba(150, 215, 215, 0.75);
    --white: #ffffff;
    --photo-yellow: #f2b23a;
    --photo-skin: #e6b8a3;
    --photo-dark: #1d1d1f;
    --photo-grey: #9aa0a6;
    --photo-wood: #d8b27c;
    --flag-red: #8d2a33;
    --flag-navy: #2b3556;
    --field-green: #3d8a3a;
  }
  * { margin: 0; padding: 0; box-sizing: border-box; }
  html, body { width: 1200px; height: 771px; overflow: hidden; }
  body {
    background: linear-gradient(135deg, var(--bg-top) 0%, #5f9eb6 50%, var(--bg-bottom) 100%);
    font-family: "Hind", "Segoe UI", sans-serif;
    color: var(--white);
    position: relative;
  }
  .slide {
    position: absolute;
    width: 331px;
    height: 186px;
    overflow: hidden;
    background: linear-gradient(120deg, var(--slide-deep) 0%, var(--slide-mid) 45%, var(--slide-teal) 100%);
    box-shadow: 0 14px 22px rgba(30, 60, 90, 0.35);
  }
  .col-1 { left: 58px; } .col-2 { left: 434px; } .col-3 { left: 811px; }
  .row-1 { top: 61px; } .row-2 { top: 292px; } .row-3 { top: 523px; }

  .abs { position: absolute; }
  .field-photo {
    position: absolute; inset: 0;
    background:
      linear-gradient(180deg, rgba(74,120,168,0.85) 0%, rgba(98,160,180,0.7) 45%, rgba(120,190,170,0.75) 75%, rgba(110,170,120,0.7) 100%),
      linear-gradient(90deg, #3f6c8c, #7dbfc4);
  }
  .ring { position: absolute; border-radius: 50%; border: 4px solid var(--ring); }

  .rule { position: absolute; height: 1.5px; width: 62px; background: var(--white); }
  .rule.center { left: 50%; transform: translateX(-50%); }

  .title-main { font-family: "Lato", sans-serif; font-size: 17px; font-weight: 400; white-space: nowrap; }
  .title-sub { font-family: "Lato", sans-serif; font-size: 12.5px; font-weight: 400; white-space: nowrap; }
  .lede { font-size: 5.6px; line-height: 12.5px; }
  .body-text { font-size: 8.6px; line-height: 17.5px; font-weight: 300; letter-spacing: 0.1px; }
  .centered { left: 0; right: 0; text-align: center; }

  .photo { position: absolute; border-radius: 2px; box-shadow: 0 3px 6px rgba(20,40,60,0.3); }
  .photo-yellow { background: linear-gradient(135deg, var(--photo-yellow), #e9a52c 60%, var(--photo-skin)); }
  .photo-smile { background: linear-gradient(160deg, var(--photo-skin), #d99a86 55%, var(--photo-yellow)); }
  .photo-mono { background: linear-gradient(135deg, #2a2a2a, #8a8a8a 55%, #1a1a1a); }
  .photo-mould { background: linear-gradient(135deg, #e8d5c6, #cfe3d2 55%, #f1ece7); }
  .photo-case { background: linear-gradient(180deg, var(--photo-grey) 0%, #c9cdd1 45%, #eef0f2 55%, var(--photo-wood) 68%, #c79a5e 100%); }
  .photo-athlete { background: radial-gradient(ellipse at 55% 55%, #5a1d22 0%, var(--photo-dark) 45%), linear-gradient(180deg, var(--photo-dark) 85%, var(--field-green) 100%); }

  .hero-top {
    position: absolute; left: 0; top: 0; width: 100%; height: 125px;
  }
  .hero-guard {
    background: linear-gradient(180deg, transparent 55%, var(--slide-mid) 100%),
                linear-gradient(100deg, var(--photo-skin) 0%, #e9c0ad 55%, var(--photo-yellow) 100%);
  }
  .hero-flag {
    background: linear-gradient(180deg, transparent 45%, var(--slide-mid) 100%),
                linear-gradient(110deg, var(--flag-navy) 0%, var(--flag-navy) 30%, var(--flag-red) 45%, #c8b8a8 60%, var(--flag-red) 75%, #3a2a36 100%);
  }

  .checklist { position: absolute; left: 165px; top: 55px; list-style: none; }
  .checklist li { position: relative; padding-left: 12px; font-size: 5.7px; line-height: 7.8px; }
  .checklist svg { position: absolute; left: 0; top: 0; width: 7px; height: 7px; }

  .feature { position: absolute; left: 32px; display: flex; gap: 14px; }
  .feature svg { flex: none; width: 34px; height: 30px; }
</style>
</head>
<body>

  <!-- Slide 1: title -->
  <section class="slide col-1 row-1">
    <div class="field-photo" role="img" aria-label="Blurred soccer goal net in front of trees and a grass field"></div>
    <div class="ring" style="left:115px; top:46px; width:100px; height:100px;"></div>
    <h1 class="abs title-main centered" style="top:82px;">Mouthguards and Sports Safety</h1>
  </section>

  <!-- Slide 2: uniform -->
  <section class="slide col-2 row-1">
    <div class="field-photo" role="img" aria-label="Blurred soccer goal net in front of trees and a grass field"></div>
    <div class="ring" style="left:23px; top:46px; width:100px; height:100px;"></div>
    <h2 class="abs title-sub" style="left:78px; top:74px;">Make A Mouthguard Part Of Your Uniform</h2>
    <div class="rule" style="left:78px; top:95px;"></div>
    <p class="abs lede" style="left:80px; top:102px; width:240px;">When it comes to protecting your smile during active sports, a properly fitted mouthguard is a key piece of athletic gear for children and adults</p>
  </section>

  <!-- Slide 3: upper teeth -->
  <section class="slide col-3 row-1">
    <div class="photo photo-yellow" style="left:30px; top:16px; width:102px; height:73px;" role="img" aria-label="Young woman holding a clear mouthguard in front of a yellow background"></div>
    <div class="photo photo-smile" style="left:30px; top:96px; width:102px; height:73px;" role="img" aria-label="Close view of a clear mouthguard being placed on upper teeth"></div>
    <div class="rule" style="left:153px; top:73px;"></div>
    <p class="abs body-text" style="left:153px; top:81px; width:160px;">Mouthguards typically cover the upper teeth, which are more exposed than the lower teeth</p>
  </section>

  <!-- Slide 4: cushion impacts -->
  <section class="slide col-1 row-2">
    <div class="photo photo-mould" style="left:18px; top:20px; width:86px; height:53px;" role="img" aria-label="Hand holding a dental mould of teeth"></div>
    <div class="photo photo-mono" style="left:122px; top:20px; width:86px; height:53px;" role="img" aria-label="Black and white close view of a smile"></div>
    <div class="photo photo-smile" style="left:226px; top:20px; width:86px; height:53px;" role="img" aria-label="Clear mouthguard held in front of teeth"></div>
    <div class="rule center" style="top:107px;"></div>
    <p class="abs body-text centered" style="top:115px; padding:0 40px;">Mouthguards cushion impacts that may otherwise cause broken teeth, jaw injuries, or cuts to your lips, tongue, or face.</p>
  </section>

  <!-- Slide 5: contact sports -->
  <section class="slide col-2 row-2">
    <div class="hero-top hero-guard" role="img" aria-label="Close view of hands fitting a clear mouthguard over teeth"></div>
    <div class="rule center" style="top:107px;"></div>
    <p class="abs body-text centered" style="top:115px; padding:0 40px;">Mouthguards are commonly used in contact sports. However, mouthguards help prevent mouth and jaw injuries even in non contact sports</p>
  </section>

  <!-- Slide 6: checklist -->
  <section class="slide col-3 row-2">
    <div class="rule center" style="top:16px; width:34px;"></div>
    <h3 class="abs centered" style="top:23px; font-size:8px; font-weight:400; text-align:center;">Pick A Mouthguard That</h3>
    <div class="photo photo-case" style="left:18px; top:55px; width:133px; height:102px;" role="img" aria-label="Clear aligner trays resting in an open white case on a wooden table"></div>
    <ul class="checklist">
      <li style="margin-bottom:10px;"><svg viewBox="0 0 10 10" fill="none" stroke="#fff" stroke-width="0.8"><rect x="1.5" y="1.5" width="7" height="7" rx="1.5"/><path d="M3.2 5.1l1.3 1.3 2.4-2.6"/></svg>Fits properly and is comfortable</li>
      <li style="margin-bottom:2px;"><svg viewBox="0 0 10 10" fill="none" stroke="#fff" stroke-width="0.8"><circle cx="5" cy="5" r="3.6"/><path d="M3.4 5.1l1.1 1.1 2.1-2.3"/></svg>Ideally has been custom made by a dentist</li>
      <li style="margin-top:8px; margin-bottom:6px; width:140px;"><svg viewBox="0 0 10 10" fill="none" stroke="#fff" stroke-width="0.8"><path d="M2 8l3-6 3 6z"/></svg>Has enough flex that it won’t tear or break, and is thick enough to hold up to a heavy hit</li>
      <li style="margin-bottom:10px;"><svg viewBox="0 0 10 10" fill="none" stroke="#fff" stroke-width="0.8"><path d="M5 1v8M1 5h8M2.2 2.2l5.6 5.6"/></svg>Is easy to clean</li>
      <li style="margin-bottom:10px;"><svg viewBox="0 0 10 10" fill="none" stroke="#fff" stroke-width="0.8"><path d="M3 1.5v5l-1.5 2.5M3 6.5l5 2.5"/></svg>Doesn’t limit speech or breathing</li>
      <li><svg viewBox="0 0 10 10" fill="none" stroke="#fff" stroke-width="0.8"><path d="M5 1l1.2 2.6 2.8.3-2.1 1.9.6 2.8L5 7.2 2.5 8.6l.6-2.8L1 3.9l2.8-.3z"/></svg>Stays in place</li>
    </ul>
  </section>

  <!-- Slide 7: custom offer -->
  <section class="slide col-1 row-3">
    <div class="field-photo" role="img" aria-label="Blurred soccer goal net in front of trees and a grass field"></div>
    <div class="feature" style="top:55px;">
      <svg viewBox="0 0 34 30" fill="none" stroke="#fff" stroke-width="1.2">
        <circle cx="10" cy="10" r="6"/><circle cx="24" cy="11" r="5.5"/>
        <path d="M1 28v-4c0-4 4-7 9-7s9 3 9 7v4M17 28v-3c0-3.5 3-6 7-6s7 2.5 7 6v3"/>
      </svg>
      <p class="body-text" style="width:240px; font-weight:400;">We can make you or your child a custom mouthguard that is comfortable and protects the jaw.</p>
    </div>
    <div class="feature" style="top:101px;">
      <svg viewBox="0 0 34 30" fill="none" stroke="#fff" stroke-width="1.2">
        <circle cx="12" cy="10" r="8"/><path d="M8 10l3 3 6-6"/>
        <path d="M6 20h10v9H6zM16 22h6v7h-6M26 16h4v13h-4"/>
      </svg>
      <p class="body-text" style="width:240px; font-weight:400;">Ready-made mouthguards may be cheaper, but they do not fit as well and can make it harder to speak or breath</p>
    </div>
  </section>

  <!-- Slide 8: basketball stat -->
  <section class="slide col-2 row-3">
    <div class="hero-top hero-flag" role="img" aria-label="Close view of a waving stars and stripes flag"></div>
    <div class="rule center" style="top:107px;"></div>
    <p class="abs body-text centered" style="top:115px; padding:0 38px;">The National Council for Youth Dental Care says that most oral injuries among 13 through 17 year olds occur while playing basketball</p>
  </section>

  <!-- Slide 9: baseball stat -->
  <section class="slide col-3 row-3">
    <div class="photo photo-athlete" style="left:30px; top:16px; width:102px; height:153px;" role="img" aria-label="Football player in red leaping to catch a ball at night on a green field"></div>
    <div class="rule" style="left:153px; top:73px;"></div>
    <p class="abs body-text" style="left:153px; top:81px; width:165px;">Baseball accounts for most of the oral injuries in 7 through 12 year olds</p>
  </section>

</body>
</html>
```